Inspirational Quote Poster for Employees

For this project, we need a simple yet high-impact poster template that will be customized for each of our employees with a personalized inspirational quote and color scheme. This template should allow us to quickly and easily customize the text and colors in the poster without a lot of effort.

The poster design should consist of:
- A stylized text area to contain the main text of the quote
- A separate text area to contain the source of quote
- A background that complements the color and style of the text

Text may use different typographic effects (such as color, stroke weight, italicization, font size changes, drop shadows) to draw attention to words in the quote; the source of the quote may be formatted the same as the main text of the quote, or may be formatted differently to distinguish it from the main quote.

The background may be simply a single color, subtle texture, gradients, halftone effects, or other color/texture effects may be used to complement the text.

Examples of the types of posters envisioned by this project:
- http://www.pinvelora.example/marcusdtelford/quillbase-job-1/

Sample quotes to use to build your poster - choose whichever one you want, but be certain that the poster design will handle both long and short quotes:
- "Happiness in intelligent people is the rarest thing I know" - Walden Prosket
- "Wanting to be someone else is a waste of the person you are." - Rolf Dintey
- "Experience is not what happens to you. It is what you do with what happens to you." - Ferris Mundell
- "Simplicity is the ultimate in sophistication." - Rinaldo de Pavesco
- "You will get all you want in life if you help enough other people get what they want." - Tad Pomfrey
- "Hell, there are no rules here — we're trying to accomplish something." - Gareth Vullane

Industry/Entity Type

Quote

Requirements
Must have
• Final deliverable must be:
• - Formatted for an 18” x 24” poster (in portrait orientation)
• - Delivered in Adobe InDesign, Adobe Illustrator, or Extended PostScript format
• - Use CMYK color mode
• - Be print-ready at 300dpi resolution
• - Include any fonts used in the template

```html
<!DOCTYPE html>
<html lang="en">
<head>
<meta charset="utf-8">
<title>Quote Poster</title>
<link rel="stylesheet" href="https://fonts.googleapis.com/css2?family=Barlow+Semi+Condensed:wght@400;700&display=swap">
<style>
  :root {
    --poster-bg: #ffe000;
    --ink: #1b1a17;
  }
  html, body {
    margin: 0;
    padding: 0;
    overflow: hidden;
  }
  body {
    width: 849px;
    height: 1200px;
    background: var(--poster-bg);
  }
  .poster {
    position: relative;
    width: 849px;
    height: 1200px;
    background: var(--poster-bg);
    color: var(--ink);
    font-family: "Barlow Semi Condensed", "Arial Narrow", sans-serif;
  }
  .quote {
    position: absolute;
    left: 97px;
    top: 420px;
    margin: 0;
    font-weight: 700;
    font-size: 80px;
    line-height: 76px;
    letter-spacing: -0.5px;
    text-transform: uppercase;
  }
  .quote-line {
    display: block;
    white-space: nowrap;
  }
  .source {
    position: absolute;
    left: 98px;
    top: 786px;
    margin: 0;
    font-weight: 400;
    font-size: 21px;
    letter-spacing: 0.3px;
    text-transform: uppercase;
  }
</style>
</head>
<body>
  <main class="poster">
    <blockquote class="quote">
      <span class="quote-line">Happiness in</span>
      <span class="quote-line">intelligent people</span>
      <span class="quote-line">is the rarest thing</span>
      <span class="quote-line">I know</span>
    </blockquote>
    <p class="source">Walden Prosket</p>
  </main>
</body>
</html>
```